International tradind company needs a professional Business Card

We are an international trading company and we need a business card for our CEO and employers so they can give it away in their meetings and while networking.
We want the card design quality to cause an immediate "wow" and we count on you to do that!

key-words and concepts to communicate: trustworthiness, ethics, sucess, modern, global business, networking

Our favorite colours are blue and grey but we are open to suggestions.

It would be recommended that our logo was part of the card. You can see it in www.kovendagroup.com . We also would like the following info on the card:
Name
position in the company
cell phone and personal email

```html
<!DOCTYPE html>
<html lang="en">
<head>
<meta charset="utf-8">
<title>Kovenda Group – Business Card</title>
<link href="https://fonts.googleapis.com/css2?family=Open+Sans:wght@400;600&family=Questrial&display=swap" rel="stylesheet">
<style>
  :root {
    --backdrop: #d9d9d6;
    --card-dark: #000000;
    --card-light: #ffffff;
    --ink-light: #ffffff;
    --brand-navy: #2a1f6b;
    --brand-blue: #3f7fc7;
    --text-dark: #1b1b1b;
    --rule: #8a8a8a;
  }
  * { margin: 0; padding: 0; box-sizing: border-box; }
  html, body {
    width: 1200px; height: 900px; overflow: hidden;
    background: var(--backdrop);
  }
  .canvas { position: relative; width: 1200px; height: 900px; }

  .card {
    position: absolute; left: 280px; width: 640px; height: 376px;
    border-radius: 20px;
  }
  .card--front { top: 50px; background: var(--card-dark); }
  .card--back { top: 463px; background: var(--card-light); }

  .brand-mark {
    position: absolute; border-radius: 50%;
  }
  .card--front .brand-mark {
    left: 80px; top: 118px; width: 110px; height: 110px;
    background: var(--ink-light);
  }
  .card--back .brand-mark {
    left: 290px; top: 98px; width: 76px; height: 76px;
    background: var(--brand-blue);
  }

  .brand-name, .brand-tagline {
    position: absolute; font-family: "Open Sans", sans-serif;
    font-weight: 400; white-space: nowrap; line-height: 1;
  }
  .card--front .brand-name {
    left: 256px; top: 140px; font-size: 50px; color: var(--ink-light);
    letter-spacing: -0.5px;
  }
  .card--front .brand-tagline {
    left: 258px; top: 202px; font-size: 27px; color: var(--ink-light);
  }
  .card--back .brand-name {
    left: 402px; top: 111px; font-size: 32px; color: var(--brand-navy);
    letter-spacing: -0.3px;
  }
  .card--back .brand-tagline {
    left: 403px; top: 151px; font-size: 18px; color: var(--brand-blue);
  }

  .contact {
    position: absolute; font-family: "Questrial", sans-serif;
    font-size: 15px; line-height: 20px; color: var(--text-dark);
    letter-spacing: 0.2px;
  }
  .contact--person { left: 41px; top: 246px; }
  .contact--office { left: 397px; top: 247px; }
  .contact__name { font-size: 17px; font-weight: 600; font-family: "Open Sans", sans-serif; }
  .contact__gap { height: 20px; }

  .divider {
    position: absolute; left: 280px; top: 249px; width: 1px; height: 96px;
    background: var(--rule);
  }
</style>
</head>
<body>
<main class="canvas">
  <section class="card card--front" aria-label="Card front">
    <div class="brand-mark"></div>
    <div class="brand-name">Kovenda Group</div>
    <div class="brand-tagline">Business Services</div>
  </section>

  <section class="card card--back" aria-label="Card back">
    <div class="brand-mark"></div>
    <div class="brand-name">Kovenda Group</div>
    <div class="brand-tagline">Business Services</div>

    <div class="contact contact--person">
      <div class="contact__name">Marco Teles</div>
      <div>CEO</div>
      <div class="contact__gap"></div>
      <div>+351 912407315</div>
      <div>marco@kovendagroup.com</div>
    </div>

    <div class="divider"></div>

    <div class="contact contact--office">
      <div>Rua das Flores, 18, 2o Esq</div>
      <div>1200-195 Lisboa</div>
      <div>T: +351 210457382</div>
      <div>E: contact@kovendagroup.com</div>
      <div>W: www.kovendagroup.com</div>
    </div>
  </section>
</main>
</body>
</html>
```